A modern web page for a software product

We need a web page for a software product, which is an advanced solution based on Machine Learning and Natural Language processing. We already have a logo of the product and expect the web page to be inline with the logo colors. The design should be for one page web site with scrolled sections - details of the content and guidelines in the attachments.

Target Market(s)

software company

Industry/Entity Type

It Company

Number of Pages Required

1 page

Colors

Designer to choose colors to be used in the design.

Requirements
Must have
• - modern icons and graphics
• - inline with the logo colors
• - be related to Machine Learining, AI, data processing
• - should have two language versions: english and polish both are attached.
Nice to have
• - animation/motion
Should not have
• - any photos embedded

```html
<!DOCTYPE html>
<html lang="en">
<head>
<meta charset="utf-8">
<title>Sorteq – Discovery and Classification of personal data</title>
<link href="https://fonts.googleapis.com/css2?family=Open+Sans:wght@400;600;700&family=Roboto+Condensed:wght@400;700&display=swap" rel="stylesheet">
<style>
  :root{
    --navy:#1b3a66;
    --teal:#1fb5ac;
    --text:#3a3a3a;
    --muted:#555;
    --white:#ffffff;
    --hero-dark:#0b0b0d;
    --band-blue:#1c5ca8;
    --band-deep:#1f3c93;
    --footer:#0c0c0c;
    --line:#cfd6dc;
  }
  *{margin:0;padding:0;box-sizing:border-box}
  html,body{width:1200px;height:2736px;overflow:hidden}
  body{position:relative;background:var(--white);font-family:"Open Sans",sans-serif;color:var(--text)}
  .abs{position:absolute}

  /* header */
  .site-header{position:absolute;left:0;top:0;width:1200px;height:119px;background:var(--white)}
  .brand{position:absolute;left:90px;top:34px;display:flex;align-items:center;gap:12px;font-family:"Roboto Condensed",sans-serif;font-weight:700;font-size:40px;color:var(--navy);line-height:1}
  .brand-mark{width:30px;height:30px;background:var(--teal)}
  .nav a{position:absolute;top:46px;font-size:17px;color:var(--text);text-decoration:none}
  .nav a.active{color:var(--navy)}
  .lang-btn{position:absolute;left:1000px;top:36px;width:111px;height:42px;background:var(--teal);color:var(--white);font-size:14px;display:flex;align-items:center;justify-content:center;gap:6px;border-radius:2px}

  /* hero */
  .hero{position:absolute;left:0;top:119px;width:1200px;height:507px;background:linear-gradient(90deg,#2a2a30 0%,#15151a 45%,var(--hero-dark) 70%)}
  .hero-art{position:absolute;left:0;top:0;width:720px;height:507px;background:radial-gradient(ellipse 260px 190px at 420px 220px,#b08a1e 0%,#5e4a16 40%,rgba(30,30,34,0) 100%)}
  .hero-title{position:absolute;left:766px;top:300px;font-family:"Roboto Condensed",sans-serif;font-size:60px;color:var(--white);white-space:nowrap}
  .hero-sub{position:absolute;left:766px;top:378px;font-family:"Roboto Condensed",sans-serif;font-size:29px;color:var(--white)}
  .hero-arrows{position:absolute;left:1058px;top:530px;display:flex;gap:4px}
  .hero-arrows span{width:24px;height:24px;border-radius:50%;background:#1a1a1a;display:flex;align-items:center;justify-content:center}

  /* features */
  .features-frame{position:absolute;left:140px;top:719px;width:336px;height:315px;background:var(--teal)}
  .features-art{position:absolute;left:162px;top:742px;width:336px;height:316px;background:linear-gradient(160deg,#dfe6ee 0%,#b9c6d6 55%,#8fa3bd 100%)}
  .features-title{position:absolute;left:544px;top:746px;font-family:"Roboto Condensed",sans-serif;font-size:36px;color:#111}
  .features-list{position:absolute;left:544px;top:806px;list-style:none}
  .features-list li{font-size:15px;color:var(--muted);height:34.7px;line-height:22px;padding-left:18px;position:relative}
  .features-list li::before{content:"»";position:absolute;left:0;top:0;color:#666}

  /* use cases */
  .use-cases{position:absolute;left:0;top:1156px;width:1200px;height:493px;background:linear-gradient(100deg,#1f7fae 0%,var(--band-blue) 45%,var(--band-deep) 100%)}
  .section-title-light{position:absolute;width:1200px;text-align:center;font-family:"Roboto Condensed",sans-serif;font-size:34px;color:var(--white)}
  .case-card{position:absolute;top:175px;width:294px;height:223px;border:1px solid rgba(255,255,255,.55);background:rgba(8,40,70,.45);color:var(--white);text-align:center;padding:0 30px}
  .case-card svg{display:block;margin:42px auto 28px}
  .case-card p{font-size:14px;line-height:20px}
  .case-arrow{position:absolute;top:260px}

  /* highlights */
  .highlights-title{position:absolute;width:1200px;top:1730px;text-align:center;font-family:"Roboto Condensed",sans-serif;font-size:36px;color:#111}
  .highlights-art{position:absolute;left:113px;top:1824px;width:365px;height:346px;background:linear-gradient(140deg,#dff0e9 0%,#f6e3c8 50%,#d7e4f0 100%);border-radius:6px}
  .timeline{position:absolute;left:0;top:0}
  .hl-title{position:absolute;font-size:20px;color:#222}
  .hl-subs{position:absolute;left:627px;top:1878px;list-style:none}
  .hl-subs li{font-size:13px;color:#666;height:21px}

  /* contact */
  .contact{position:absolute;left:0;top:2298px;width:1200px;height:296px;background:linear-gradient(100deg,#1f4f9c 0%,#1c6aa6 50%,#22a7a8 100%);color:var(--white);text-align:center}
  .contact-line{position:absolute;width:1200px;font-size:18px}

  /* footer */
  .site-footer{position:absolute;left:0;top:2594px;width:1200px;height:142px;background:var(--footer);color:var(--white)}
  .social{position:absolute;left:527px;top:30px;display:flex;gap:14px}
  .social span{width:26px;height:26px;background:var(--white);border-radius:4px}
  .copyright{position:absolute;width:1200px;top:80px;text-align:center;font-size:14px}
</style>
</head>
<body>

<header class="site-header">
  <div class="brand"><span class="brand-mark"></span>Sorteq</div>
  <nav class="nav">
    <a class="active" style="left:482px">Home</a>
    <a style="left:582px">Features</a>
    <a style="left:697px">Cases</a>
    <a style="left:779px">Highlights</a>
    <a style="left:905px">Contact</a>
  </nav>
  <div class="lang-btn">ENGLISH
    <svg width="9" height="6" viewBox="0 0 9 6"><path d="M1 1l3.5 3.5L8 1" stroke="#fff" stroke-width="1.6" fill="none"/></svg>
  </div>
</header>

<section class="hero">
  <div class="hero-art" role="img" aria-label="Glowing AI brain with circuit lines resting above an open hand"></div>
  <h1 class="hero-title">Discovery and</h1>
  <p class="hero-sub">Classification of personal data</p>
  <div class="hero-arrows">
    <span><svg width="10" height="10" viewBox="0 0 10 10"><path d="M6.5 1.5L3 5l3.5 3.5" stroke="#fff" stroke-width="1.6" fill="none"/></svg></span>
    <span><svg width="10" height="10" viewBox="0 0 10 10"><path d="M3.5 1.5L7 5l-3.5 3.5" stroke="#fff" stroke-width="1.6" fill="none"/></svg></span>
  </div>
</section>

<section class="features">
  <div class="features-frame"></div>
  <div class="features-art" role="img" aria-label="White humanoid robot sitting in a thinking pose on a light blue background"></div>
  <h2 class="features-title">FEATURES</h2>
  <ul class="features-list">
    <li>Detection of personal and sensitive data for GDPR compliance</li>
    <li>Fast cataloging and classification of data and sources</li>
    <li>Unified data registry for RODO compliance fulfilment</li>
    <li>Management of consents and data access policies</li>
    <li>Customizable analytics and reporting</li>
    <li>Ability to integrates with tools for data anonymization or depersonalization</li>
    <li>RESTful API for system management and integration</li>
  </ul>
</section>

<section class="use-cases">
  <h2 class="section-title-light" style="top:88px">Use Cases</h2>
  <svg class="case-arrow" style="left:56px" width="16" height="30" viewBox="0 0 16 30"><path d="M13 2L3 15l10 13" stroke="#9fd8e6" stroke-width="2" fill="none"/></svg>
  <svg class="case-arrow" style="left:1120px" width="16" height="30" viewBox="0 0 16 30"><path d="M3 2l10 13L3 28" stroke="#9fd8e6" stroke-width="2" fill="none"/></svg>

  <div class="case-card" style="left:122px">
    <svg width="46" height="40" viewBox="0 0 46 40"><rect x="2" y="2" width="42" height="28" rx="2" fill="none" stroke="#fff" stroke-width="4"/><rect x="17" y="31" width="12" height="5" fill="#fff"/><rect x="11" y="35" width="24" height="4" fill="#fff"/></svg>
    <p>Internal audits and verification of the current status - in preparation for ensuring RODO compliance</p>
  </div>
  <div class="case-card" style="left:452px">
    <svg width="44" height="48" viewBox="0 0 44 48"><ellipse cx="22" cy="7" rx="20" ry="6" fill="#fff"/><path d="M2 12c0 8 40 8 40 0v8c0 8-40 8-40 0z" fill="#fff"/><path d="M2 25c0 8 40 8 40 0v8c0 8-40 8-40 0z" fill="#fff"/><path d="M2 38c0 6 40 6 40 0v3c0 8-40 8-40 0z" fill="#fff"/></svg>
    <p>Cataloging sources that store sensitive data</p>
  </div>
  <div class="case-card" style="left:781px">
    <svg width="46" height="40" viewBox="0 0 46 40"><circle cx="23" cy="9" r="7" fill="#fff"/><circle cx="9" cy="13" r="5" fill="#fff"/><circle cx="37" cy="13" r="5" fill="#fff"/><path d="M11 38c0-12 24-12 24 0z" fill="#fff"/><path d="M0 34c0-9 13-10 16-5l-3 5z" fill="#fff"/><path d="M46 34c0-9-13-10-16-5l3 5z" fill="#fff"/></svg>
    <p>Keeping the registry of personal data in order to implement rights to information, forgetfulness, data transfer</p>
  </div>
</section>

<section class="highlights">
  <h2 class="highlights-title">Highlights</h2>
  <div class="highlights-art" role="img" aria-label="Illustration of a monitor and tablet showing bar and pie charts with a magnifying glass and clouds"></div>

  <svg class="timeline" width="1200" height="2736" viewBox="0 0 1200 2736">
    <line x1="571" y1="1913" x2="571" y2="2136" stroke="var(--line)" stroke-width="2"/>
    <circle cx="571" cy="1875" r="38" fill="#fff" stroke="var(--line)" stroke-width="2"/>
    <circle cx="565" cy="1870" r="7" fill="none" stroke="var(--teal)" stroke-width="4"/>
    <circle cx="579" cy="1882" r="5" fill="none" stroke="var(--teal)" stroke-width="3"/>
    <circle cx="571" cy="2008" r="28" fill="#fff" stroke="var(--line)" stroke-width="2"/>
    <circle cx="571" cy="2003" r="5" fill="var(--teal)"/>
    <path d="M562 2017c0-8 18-8 18 0z" fill="var(--teal)"/>
    <circle cx="571" cy="2072" r="28" fill="#fff" stroke="var(--line)" stroke-width="2"/>
    <rect x="563" y="2062" width="11" height="14" fill="none" stroke="var(--teal)" stroke-width="2"/>
    <rect x="568" y="2068" width="11" height="14" fill="var(--teal)"/>
    <circle cx="571" cy="2136" r="28" fill="#fff" stroke="var(--line)" stroke-width="2"/>
    <path d="M561 2137l20-9-7 19-3-7z" fill="var(--teal)"/>
  </svg>

  <p class="hl-title" style="left:627px;top:1840px">Built in support for detection of Polish personal data</p>
  <ul class="hl-subs">
    <li>a. sensitive data type (eg.:ID, name, address, etc.)</li>
    <li>b. context of data occurrence</li>
    <li>c. metadata describing the data source (e.g. system, table, author, etc.)</li>
    <li>d. metadata describing the detection process</li>
  </ul>
  <p class="hl-title" style="left:631px;top:1994px">High effectiveness of personal data detection</p>
  <p class="hl-title" style="left:629px;top:2058px">Supports structured and unstructured data source</p>
  <p class="hl-title" style="left:629px;top:2121px">Ready for high performance processing</p>
</section>

<section class="contact">
  <h2 class="section-title-light" style="top:62px">Contact</h2>
  <p class="contact-line" style="top:127px">Address : 27 Harbor Row,&nbsp; Milbrook, OR 97031</p>
  <p class="contact-line" style="top:164px">phone: 555-014-2290</p>
  <p class="contact-line" style="top:200px">Email: hello@sorteq.example</p>
</section>

<footer class="site-footer">
  <div class="social"><span></span><span></span><span></span><span></span></div>
  <p class="copyright">Copyright © 2018&nbsp; All Rights Reserved</p>
</footer>

</body>
</html>
```